Business Card Design Project

I need a business card design for our new logo, please check the logo at the following link:
https://www.filecrate.net/s/q7rtx2pw9kd41m/FernLoop.png
The address on the business card:
Av. Gervásio Tavares 418 sala 207
Barra da Tijuca, Rio de Janeiro, RJ
CEP: 22714-380
Brasil
Phone: +55 21 86347215
e-mail: osvaldo@fernloop.com.br
Updates
Thank you all for sending your designs, we will not provide feedback because there are too many designs, on December 3 we will pick the best design according to our point of view. Please keep posting.
Osvaldo
Industry/Entity Type
Business
Look and feel
Each slider illustrates characteristics of the customer's brand and the style your logo design should communicate.

```html
<!DOCTYPE html>
<html lang="pt-BR">
<head>
<meta charset="utf-8">
<title>FernLoop – Business Card</title>
<link href="https://fonts.googleapis.com/css2?family=Lato:wght@300;400;700;900&display=swap" rel="stylesheet">
<style>
  :root {
    --stage: #c9d1d6;
    --card-dark: #333335;
    --card-yellow: #f7c600;
    --accent: #f2bf00;
    --ink-light: #ffffff;
    --ink-soft: #e4e4e4;
    --ink-dark: #2b2b2b;
  }
  * { margin: 0; padding: 0; box-sizing: border-box; }
  html, body {
    width: 1200px;
    height: 960px;
    overflow: hidden;
    background: var(--stage);
    font-family: "Lato", Arial, sans-serif;
  }
  .canvas {
    position: relative;
    width: 1200px;
    height: 960px;
  }
  .card {
    position: absolute;
    left: 330px;
    width: 540px;
    height: 310px;
    border-radius: 3px;
    overflow: hidden;
    box-shadow: 0 10px 30px rgba(0, 0, 0, 0.18);
  }
  /* Front side */
  .card-front {
    top: 140px;
    background: var(--card-dark);
    color: var(--ink-light);
  }
  .person-name {
    position: absolute;
    left: 48px;
    top: 58px;
    font-size: 29px;
    font-weight: 300;
    letter-spacing: 0.2px;
    white-space: nowrap;
  }
  .name-rule {
    position: absolute;
    left: 0;
    top: 100px;
    width: 282px;
    height: 2px;
    background: var(--accent);
  }
  .person-role {
    position: absolute;
    left: 52px;
    top: 108px;
    font-size: 17px;
    font-weight: 400;
    color: var(--ink-soft);
    white-space: nowrap;
  }
  .contact {
    position: absolute;
    left: 318px;
    top: 64px;
    font-size: 13px;
    line-height: 18px;
    color: var(--ink-soft);
    white-space: nowrap;
  }
  .address {
    position: absolute;
    left: 326px;
    top: 188px;
    font-size: 12.5px;
    line-height: 19px;
    color: var(--ink-soft);
    font-style: normal;
    white-space: nowrap;
  }
  .brand-front {
    position: absolute;
    left: 52px;
    top: 222px;
    display: flex;
    align-items: center;
    gap: 10px;
  }
  .brand-front .brand-dot {
    width: 16px;
    height: 16px;
    background: var(--accent);
  }
  .brand-front .brand-name {
    font-size: 30px;
    font-weight: 900;
    color: var(--ink-light);
  }
  /* Back side */
  .card-back {
    top: 510px;
    background: var(--card-yellow);
    display: flex;
    align-items: center;
    justify-content: center;
    gap: 16px;
  }
  .card-back .brand-dot {
    width: 30px;
    height: 30px;
    background: var(--ink-dark);
  }
  .card-back .brand-name {
    font-size: 66px;
    font-weight: 900;
    color: var(--ink-dark);
    letter-spacing: 0.5px;
  }
</style>
</head>
<body>
  <main class="canvas">
    <section class="card card-front" aria-label="Business card front">
      <h1 class="person-name">Lúcia Fernandes</h1>
      <div class="name-rule"></div>
      <p class="person-role">Operation manager</p>
      <p class="contact">
        +55 21 86347215<br>
        osvaldo@fernloop.com.br
      </p>
      <address class="address">
        Av. Gervásio Tavares 418 sala 207<br>
        Barra da Tijuca, Rio de Janeiro, RJ<br>
        CEP: 22714-380<br>
        Brasil
      </address>
      <div class="brand-front">
        <span class="brand-dot"></span>
        <span class="brand-name">FernLoop</span>
      </div>
    </section>

    <section class="card card-back" aria-label="Business card back">
      <span class="brand-dot"></span>
      <span class="brand-name">FernLoop</span>
    </section>
  </main>
</body>
</html>
```